women's junior contemporary apparel company.
We are looking for a business card that represents our urban design aesthetic. We would like to keep it simple and modern/contemporary.
the name of the company is 'v-lanza'.

we've attached a font style but you are not limited solely to use this font. All suggestions are welcomed.

```html
<!DOCTYPE html>
<html lang="en">
<head>
<meta charset="utf-8">
<title>v-lanza business card</title>
<link href="https://fonts.googleapis.com/css2?family=Montserrat:wght@300;400;500&display=swap" rel="stylesheet">
<style>
  :root {
    --backdrop: #1c1c1c;
    --card: #f2f2f0;
    --ink: #3a3a3a;
    --ink-soft: #555555;
    --rule: #9a9a9a;
  }
  * { box-sizing: border-box; margin: 0; padding: 0; }
  html, body {
    width: 1200px; height: 900px; overflow: hidden;
    background: var(--backdrop);
    font-family: "Montserrat", Arial, sans-serif;
    color: var(--ink);
  }
  .canvas { position: relative; width: 1200px; height: 900px; }
  .card {
    position: absolute;
    width: 490px; height: 280px;
    background: var(--card);
    border-radius: 24px;
  }
  .card--contact { left: 580px; top: 130px; }
  .card--front { left: 130px; top: 480px; }

  /* contact side */
  .contact {
    position: absolute; left: 130px; top: 38px; width: 300px;
    text-align: center;
  }
  .contact__name {
    font-weight: 400; font-size: 17px; letter-spacing: 4px;
    padding-bottom: 9px; border-bottom: 1px solid var(--rule);
  }
  .contact__address {
    margin-top: 12px; font-size: 11.5px; line-height: 1.4;
    font-weight: 400; color: var(--ink-soft);
  }
  .contact__lines {
    margin-top: 24px; font-size: 11.5px; line-height: 1.45;
    color: var(--ink-soft);
  }
  .contact__brand {
    position: absolute; right: 70px; bottom: 36px;
    font-size: 30px; font-weight: 400; color: var(--ink);
    letter-spacing: 0.5px;
  }

  /* front side */
  .front {
    position: absolute; inset: 0;
    display: flex; flex-direction: column; align-items: center; justify-content: center;
  }
  .front__brand {
    font-size: 76px; font-weight: 400; color: var(--ink); line-height: 1;
  }
  .front__url {
    margin-top: 22px; font-size: 13px; letter-spacing: 1.5px; color: var(--ink);
  }
</style>
</head>
<body>
<main class="canvas">
  <section class="card card--contact">
    <div class="contact">
      <h1 class="contact__name">MARISA VELL</h1>
      <p class="contact__address">Orchard Lane 24 No.1180<br>Brookfield Row CA 54321<br>LARKMOOR</p>
      <p class="contact__lines">P: 0198765432 &nbsp;//&nbsp; F: 298765431<br>info@vlanza.com &nbsp;//&nbsp; www.vlanza.com</p>
    </div>
    <span class="contact__brand">v-lanza</span>
  </section>

  <section class="card card--front">
    <div class="front">
      <span class="front__brand">v-lanza</span>
      <span class="front__url">www.vlanza.com</span>
    </div>
  </section>
</main>
</body>
</html>
```